The Brightwater Hour with Dale Morrow

Create Podcast Art for Podvale. My podcast is about overcoming adversities.

Everyone's adversity is different and there's no one-size-fits-all solution, but when you hear someone's else's story of resilience and add a little salt to it, you can find the inspiration you need to write a new ending to your struggle.

Maybe you're going through something right now and you're afraid:

● You won't be successful
● People are talking behind your back
● You'll never get the help you need
● You're not a good husband or wife
● Your child is out of control and you'll never get through to him or her
● There isn't a light at the end of your tunnel
● You'll never get your finances out of the red
● Your spouse won't ever see things your way
● The world is never gonna change

Every story we tell on The Brightwater Hour podcast challenges those thoughts, because everyday people going through everyday stuff just like you show us otherwise.

This podcast is for you. And, it's different.

Most interviews I do, I try to go on location and interview in person.

You might not see us together on the screen,
but you'll sense the raw sincerity and closeness of a side-by-side interview through your speakers.

The colors I have chosen below are close to the website colors. If you need a better view of that go here http://www.dalemorrowvoice.com

I've attached two pictures for the podcast. I'm not sure which one to use just yet so I put them both here to see what i created by your great people!

Target Market(s)

People who are currently going through an Advesirty or have been through one. 28 - 40 age group.

Colors
ec1f27
ffffff
000000
fbee3e

Requirements
Must have
• Eye appeal and The title "The Brightwater Hour" with Dale Morrow
• HAS to be stand-out, and it HAS to give a great first impression.
Nice to have
• The colors I have chosen are close to the website colors.

```html
<!DOCTYPE html>
<html lang="en">
<head>
<meta charset="utf-8">
<title>The Brightwater Hour with Dale Morrow, Podcast Art</title>
<link rel="stylesheet" href="https://fonts.googleapis.com/css2?family=Arimo:wght@400;700&family=Rokkitt:wght@800&display=swap">
<style>
  :root {
    --brand-red: #ec1f27;
    --brand-yellow: #fbee3e;
    --brand-black: #000000;
    --brand-white: #ffffff;
    --credit-outline: #7a0c10;
  }
  html, body {
    margin: 0;
    padding: 0;
    width: 1200px;
    height: 1200px;
    overflow: hidden;
    background: var(--brand-red);
  }
  .podcast-art {
    display: block;
    width: 1200px;
    height: 1200px;
    background: var(--brand-red);
  }
  .sticker-box { fill: var(--brand-yellow); stroke: var(--brand-black); stroke-width: 5; }
  .title-text {
    font-family: "Arimo", Arial, sans-serif;
    font-weight: 400;
    font-size: 88px;
    fill: var(--brand-black);
  }
  .tagline-text {
    font-family: "Arimo", Arial, sans-serif;
    font-weight: 700;
    font-size: 86px;
    letter-spacing: -3px;
    fill: var(--brand-black);
  }
  .mic-icon-arc { fill: none; stroke: var(--brand-white); stroke-width: 10; stroke-linecap: round; }
  .mic-icon-body { fill: var(--brand-white); }
  .mic-icon-grille { stroke: var(--brand-red); stroke-width: 6; }
  .badge-oval { fill: var(--brand-black); stroke: var(--brand-white); stroke-width: 5; }
  .badge-name {
    font-family: "Arimo", Arial, sans-serif;
    font-weight: 700;
    font-size: 100px;
    fill: var(--brand-white);
  }
  .host-line {
    font-family: "Rokkitt", "Courier New", serif;
    font-weight: 800;
    fill: var(--brand-white);
    stroke: var(--credit-outline);
    stroke-width: 4;
    paint-order: stroke;
  }
  .host-with { font-size: 66px; }
  .host-name { font-size: 82px; }
</style>
</head>
<body>
<svg class="podcast-art" viewBox="0 0 1200 1200" xmlns="http://www.w3.org/2000/svg" aria-label="The Brightwater Hour with Dale Morrow podcast art">

  <g class="community-badge" transform="rotate(-14 600 905)">
    <ellipse class="badge-oval" cx="600" cy="905" rx="560" ry="235"/>
  </g>
  <g class="badge-wordmark" transform="rotate(-8 470 960)">
    <text class="badge-name" x="470" y="995" text-anchor="middle">Standwell</text>
  </g>

  <g class="title-block">
    <rect class="sticker-box" x="66" y="28" width="818" height="318"/>
    <text class="title-text" x="475" y="150" text-anchor="middle">"The Brightwater</text>
    <text class="title-text" x="475" y="290" text-anchor="middle">Hour" ?</text>
  </g>

  <g class="tagline-block" transform="rotate(3 645 505)">
    <rect class="sticker-box" x="170" y="395" width="950" height="220"/>
    <text class="tagline-text" x="645" y="535" text-anchor="middle">WE STAND BY YOU</text>
  </g>

  <g class="mic-icon" transform="translate(1040 300)">
    <path class="mic-icon-arc" d="M-46 -44 A64 64 0 0 1 46 -44"/>
    <path class="mic-icon-arc" d="M-68 -66 A96 96 0 0 1 68 -66"/>
    <path class="mic-icon-arc" d="M-68 44 A92 92 0 0 1 -68 -40"/>
    <path class="mic-icon-arc" d="M68 -40 A92 92 0 0 1 68 44"/>
    <circle class="mic-icon-body" cx="0" cy="-22" r="17"/>
    <rect class="mic-icon-body" x="-17" y="2" width="34" height="104" rx="8"/>
    <line class="mic-icon-grille" x1="-15" y1="26" x2="15" y2="26"/>
    <line class="mic-icon-grille" x1="-15" y1="46" x2="15" y2="46"/>
    <line class="mic-icon-grille" x1="-15" y1="66" x2="15" y2="66"/>
    <line class="mic-icon-grille" x1="-15" y1="86" x2="15" y2="86"/>
  </g>

  <g class="host-credit" transform="rotate(-26 950 1080)">
    <text class="host-line host-with" x="870" y="1010" text-anchor="middle">with</text>
    <text class="host-line host-name" x="955" y="1100" text-anchor="middle">Dale Morrow</text>
  </g>
</svg>
</body>
</html>
```